Energy trading company (Voltrisa) needs a business card

We need a business card for a company based in Central America. Our main purpose is trading energy . We already have the logo but we need some good creativity to design a high impact business card. Colors blue, orange, green can be used or we would like to see good combinatios with our logo

Target Market(s)

Energy

Industry/Entity Type

Power Generation

Contact Information for Business Card

Logo , headquarters , name, background

Font styles to use
Serif
Sans Serif

Colors

Designer to choose colors to be used in the design.

Requirements
Must have
• it must have a fresh and clean view
Nice to have
• good backgrounds that combine with the logo
Should not have
• too much words

```html
<!DOCTYPE html>
<html lang="en">
<head>
<meta charset="utf-8">
<title>Voltrisa Business Card</title>
<link rel="stylesheet" href="https://fonts.googleapis.com/css2?family=Mulish:wght@500&family=Bebas+Neue&family=Roboto:wght@400&display=swap">
<style>
  :root {
    --orange: #f69322;
    --white: #ffffff;
    --ink: #111111;
    --backdrop: #5e4631;
  }
  * { margin: 0; padding: 0; box-sizing: border-box; }
  html, body { width: 1189px; height: 1200px; overflow: hidden; }
  body { background: var(--backdrop); position: relative; }

  .card {
    position: absolute;
    left: 171px;
    width: 856px;
    height: 488px;
    box-shadow: 0 6px 18px rgba(0,0,0,0.45);
  }
  .card--front {
    top: 67px;
    background: var(--orange);
    border-radius: 49px 0 49px 0;
  }
  .card--back {
    top: 626px;
    background: var(--white);
    border-radius: 0 49px 0 49px;
  }

  .brand-mark {
    position: absolute;
    border-radius: 50%;
  }
  .card--front .brand-mark {
    left: 372px; top: 145px; width: 114px; height: 114px;
    background: var(--white);
  }
  .card--back .brand-mark {
    left: 376px; top: 76px; width: 106px; height: 106px;
    background: var(--orange);
  }

  .brand-name {
    position: absolute;
    left: 0; width: 100%;
    text-align: center;
    font-family: "Mulish", sans-serif;
    font-weight: 500;
    letter-spacing: 1px;
    line-height: 1;
  }
  .card--front .brand-name { top: 271px; font-size: 90px; color: var(--white); }
  .card--back .brand-name { top: 190px; font-size: 84px; color: var(--orange); }

  .person {
    position: absolute;
    right: 461px;
    top: 346px;
    text-align: right;
    font-family: "Bebas Neue", sans-serif;
    line-height: 1;
  }
  .person__name { font-size: 46px; color: var(--orange); letter-spacing: 0.5px; }
  .person__title { font-size: 27px; color: var(--ink); margin-top: 4px; }

  .divider {
    position: absolute;
    left: 428px; top: 341px;
    width: 2px; height: 84px;
    background: var(--orange);
  }

  .contact {
    position: absolute;
    left: 469px; top: 343px;
    list-style: none;
    font-family: "Roboto", sans-serif;
    font-size: 22px;
    color: var(--ink);
  }
  .contact li { display: flex; align-items: center; height: 30px; margin-bottom: 1px; white-space: nowrap; }
  .contact svg { width: 18px; height: 18px; margin-right: 15px; flex: none; }
</style>
</head>
<body>
  <section class="card card--front">
    <div class="brand-mark"></div>
    <div class="brand-name">VOLTRISA</div>
  </section>

  <section class="card card--back">
    <div class="brand-mark"></div>
    <div class="brand-name">VOLTRISA</div>

    <div class="person">
      <div class="person__name">DANIEL REYES</div>
      <div class="person__title">MANAGING DIRECTOR</div>
    </div>

    <div class="divider"></div>

    <ul class="contact">
      <li>
        <svg viewBox="0 0 18 18" aria-hidden="true"><path d="M5 2 L7.5 2 L8 6 L6.3 7.2 C7.2 9.4 8.6 10.8 10.8 11.7 L12 10 L16 10.5 L16 13 C16 14.6 14.8 16 13 16 C7.5 16 2 10.5 2 5 C2 3.2 3.4 2 5 2 Z" fill="var(--orange)"/></svg>
        (506) 2290-4471
      </li>
      <li>
        <svg viewBox="0 0 18 18" aria-hidden="true"><rect x="1" y="4" width="16" height="11" fill="var(--orange)"/><path d="M1 4 L9 10.5 L17 4" stroke="var(--white)" stroke-width="1.5" fill="none"/></svg>
        info@voltrisamail.com
      </li>
      <li>
        <svg viewBox="0 0 18 18" aria-hidden="true"><g fill="none" stroke="var(--orange)" stroke-width="1.4"><circle cx="9" cy="9" r="7.5"/><ellipse cx="9" cy="9" rx="3.3" ry="7.5"/><line x1="1.5" y1="9" x2="16.5" y2="9"/><line x1="3" y1="5" x2="15" y2="5"/><line x1="3" y1="13" x2="15" y2="13"/></g></svg>
        www.voltrisaweb.com
      </li>
    </ul>
  </section>
</body>
</html>
```